Brindle Logistics Business Card Design

We are a trucking and warehousing company. We run freight in the US manly from the Pacific NW to TX and back up the the PNW. We also do warehousing where we store, move, and distribute freight. Looking for a clean and modern design of business card. We would like to look rich and elegant. Attached is our logo.

Industry/Entity Type

Trucking Company

Contact Information for Business Card

Looking for a clean and modern design of business card. We would like to look rich and elegant.

Font styles to use
Sans Serif

Colors

Designer to choose colors to be used in the design.

Requirements
Must have
• logo but it should not dominate the card
Should not have
• logo should not dominate the card

```html
<!DOCTYPE html>
<html lang="en">
<head>
<meta charset="utf-8">
<title>Brindle Logistics Business Card</title>
<link href="https://fonts.googleapis.com/css2?family=Montserrat:wght@400;500;600&display=swap" rel="stylesheet">
<style>
  :root {
    --brand-blue: #0a6ab3;
    --brand-blue-deep: #075794;
    --ink: #2b2b2b;
    --ink-soft: #555555;
    --card-white: #ffffff;
    --card-shade: #ececec;
    --backdrop: #d9dde1;
    --on-blue: #dfe9f3;
  }
  * { box-sizing: border-box; margin: 0; padding: 0; }
  html, body { width: 1200px; height: 900px; overflow: hidden; }
  body {
    background: var(--backdrop);
    font-family: "Montserrat", sans-serif;
    display: flex;
    flex-direction: column;
    align-items: center;
    justify-content: center;
    gap: 40px;
  }
  .card {
    position: relative;
    width: 680px;
    height: 389px;
    border-radius: 22px;
    overflow: hidden;
    box-shadow: 0 10px 28px rgba(0,0,0,0.22);
  }
  /* Front */
  .card-front {
    background: radial-gradient(ellipse at 65% 70%, var(--card-white) 35%, var(--card-shade) 100%);
  }
  .name-band {
    position: absolute;
    left: 0; top: 44px;
    width: 410px; height: 62px;
    background: var(--brand-blue);
    padding: 8px 0 0 34px;
    color: var(--card-white);
  }
  .name-band .person-name {
    font-weight: 500;
    font-size: 25px;
    letter-spacing: 0.5px;
    text-transform: uppercase;
    line-height: 1.1;
  }
  .name-band .person-role {
    font-size: 13px;
    font-weight: 400;
    margin-top: 2px;
  }
  .wordmark {
    position: absolute;
    right: 40px; top: 112px;
    display: flex;
    align-items: center;
    gap: 12px;
  }
  .wordmark .mark-dot {
    width: 16px; height: 16px;
    border-radius: 50%;
    background: var(--brand-blue);
  }
  .wordmark .mark-name {
    font-weight: 600;
    font-size: 26px;
    letter-spacing: 1px;
    color: var(--ink);
    text-transform: uppercase;
    line-height: 1.05;
  }
  .contact-list {
    position: absolute;
    left: 34px; top: 200px;
    list-style: none;
    font-size: 15px;
    color: var(--ink);
    line-height: 1.55;
  }
  .contact-list li { display: flex; align-items: center; gap: 10px; }
  .contact-list svg { width: 11px; height: 11px; fill: var(--brand-blue); flex: none; }
  .contact-list .accent { color: var(--brand-blue); }
  .address {
    position: absolute;
    right: 40px; bottom: 38px;
    text-align: right;
    font-size: 15px;
    color: var(--ink);
    line-height: 1.45;
  }
  /* Back */
  .card-back {
    background: radial-gradient(ellipse at 50% 45%, var(--brand-blue) 30%, var(--brand-blue-deep) 100%);
    display: flex;
    align-items: center;
    justify-content: center;
  }
  .back-wordmark {
    font-weight: 600;
    font-size: 44px;
    letter-spacing: 2px;
    color: var(--on-blue);
    text-transform: uppercase;
    text-align: center;
    line-height: 1.1;
  }
</style>
</head>
<body>

  <section class="card card-front">
    <div class="name-band">
      <div class="person-name">Daniel Reyes</div>
      <div class="person-role">Director</div>
    </div>

    <div class="wordmark">
      <span class="mark-dot"></span>
      <span class="mark-name">Brindle<br>Logistics, LLC</span>
    </div>

    <ul class="contact-list">
      <li>
        <svg viewBox="0 0 24 24" aria-hidden="true"><path d="M6.6 10.8a15.1 15.1 0 0 0 6.6 6.6l2.2-2.2a1 1 0 0 1 1-.25 11.4 11.4 0 0 0 3.6.57 1 1 0 0 1 1 1V20a1 1 0 0 1-1 1A17 17 0 0 1 3 4a1 1 0 0 1 1-1h3.5a1 1 0 0 1 1 1c0 1.25.2 2.46.57 3.6a1 1 0 0 1-.25 1z"/></svg>
        555.210.4837
      </li>
      <li>
        <svg viewBox="0 0 24 24" aria-hidden="true"><path d="M7 1h10a2 2 0 0 1 2 2v18a2 2 0 0 1-2 2H7a2 2 0 0 1-2-2V3a2 2 0 0 1 2-2zm0 3v14h10V4z"/></svg>
        555.310.7264
      </li>
      <li>
        <svg viewBox="0 0 24 24" aria-hidden="true"><path d="M2 4h20v16H2zm2 2v.5l8 5 8-5V6zm0 2.8V18h16V8.8l-8 5z"/></svg>
        info@brindlelogistics.com
      </li>
      <li>
        <svg viewBox="0 0 24 24" aria-hidden="true"><circle cx="12" cy="12" r="10"/></svg>
        <span>www.<span class="accent">brindlelogistics</span>.com</span>
      </li>
    </ul>

    <address class="address" style="font-style: normal;">
      1820 Cedar Hollow Road<br>
      Fullerton, CA 92831
    </address>
  </section>

  <section class="card card-back">
    <div class="back-wordmark">Brindle<br>Logistics, LLC</div>
  </section>

</body>
</html>
```